Homepage design for personal injury lawyer

NOTE: I will not close the project until June 9th. I want to give everyone time to put in their best work.
Your task is to redesign the homepage for this site:
https://corwistlane.com/
Feel free to use any images you find on the site.
I'm deliberately leaving the description simple so that I don't limit you.
Updates
Hi everyone. I will keep the project open for a few days to leave time for designs.
Number of Pages Required
1 page
Look and feel
Each slider illustrates characteristics of the customer's brand and the style your logo design should communicate.

```html
<!DOCTYPE html>
<html lang="en">
<head>
<meta charset="utf-8">
<title>Corwist Lane Injury Lawyers</title>
<link href="https://fonts.googleapis.com/css2?family=Montserrat:wght@500;600;700;800&family=Open+Sans:wght@400;600;700&display=swap" rel="stylesheet">
<style>
:root{
  --navy:#0d2545;
  --blue:#1d5fae;
  --blue-dark:#174d8f;
  --orange:#e8692a;
  --hero:#e8ecf1;
  --ink:#1b2a3e;
  --muted:#56606c;
  --white:#ffffff;
  --line:#d5dbe3;
}
*{box-sizing:border-box;margin:0;padding:0}
html,body{width:711px;height:1200px;overflow:hidden;background:var(--white)}
body{font-family:"Open Sans",Arial,sans-serif;color:var(--ink);position:relative}
.site-header{position:absolute;top:0;left:0;width:711px;height:24px;background:var(--white);display:flex;align-items:center;padding:0 14px;box-shadow:0 1px 3px rgba(0,0,0,.12);z-index:2}
.brand{display:flex;align-items:center;gap:5px;font-family:"Montserrat",sans-serif;font-weight:700;font-size:7.5px;color:var(--navy);letter-spacing:.4px;text-transform:uppercase;width:230px}
.brand-mark{width:12px;height:12px;background:var(--navy)}
.main-nav{display:flex;gap:16px;font-family:"Montserrat",sans-serif;font-size:6px;font-weight:600;color:var(--navy);text-transform:uppercase}
.header-cta{margin-left:auto;background:var(--orange);color:var(--white);font-family:"Montserrat",sans-serif;font-weight:700;font-size:7.5px;padding:4px 10px;border-radius:2px}
.hero{position:absolute;top:24px;left:0;width:711px;height:171px;background:var(--hero)}
.hero-photo{position:absolute;right:0;top:0;width:380px;height:171px;background:linear-gradient(90deg,var(--hero) 0%,#cdd4dc 35%,#9aa4b0 70%,#b7bfc9 100%)}
.hero-checks{position:absolute;left:26px;top:26px;list-style:none}
.hero-checks li{display:flex;align-items:center;gap:7px;font-family:"Montserrat",sans-serif;font-weight:700;font-size:11px;color:var(--navy);margin-bottom:4px}
.tick{width:11px;height:11px;background:var(--blue);border-radius:2px;display:flex;align-items:center;justify-content:center}
.hero-btn{position:absolute;left:26px;top:96px;background:var(--blue);color:var(--white);font-family:"Montserrat",sans-serif;font-weight:700;font-size:7.5px;padding:9px 16px;border-radius:14px;letter-spacing:.3px}
.media{position:absolute;top:186px;left:0;width:711px;height:42px;background:var(--white)}
.media-label{position:absolute;left:24px;top:2px;font-size:6px;color:var(--muted)}
.media-logos{position:absolute;left:24px;top:16px;display:flex;gap:9px;align-items:center}
.media-logos span{display:block;height:10px;background:#8a939d;border-radius:2px}
.trust{position:absolute;right:20px;top:4px;display:flex;gap:10px}
.trust-badge{width:88px;height:34px;border:1px solid var(--line);border-radius:3px;display:flex;align-items:center;justify-content:center;gap:4px}
.trust-badge i{display:block;width:22px;height:22px;border-radius:50%;background:#c9cfd6}
.trust-badge b{display:block;width:46px;height:8px;background:#dfe3e8;border-radius:2px}
.scene{position:absolute;top:228px;left:0;width:711px;height:76px;background:linear-gradient(100deg,#6e7a86 0%,#a9b2bb 40%,#d8dde2 60%,#7f8a95 100%)}
.practice-bar{position:absolute;top:304px;left:0;width:711px;height:42px;background:var(--navy);padding:6px 22px;display:flex;flex-wrap:wrap;align-content:flex-start;row-gap:4px}
.practice-bar a{color:var(--white);text-decoration:none;font-size:5.5px;font-weight:600;text-transform:uppercase;width:166px;border:1px solid rgba(255,255,255,.25);padding:3px 6px}
.intro{position:absolute;top:346px;left:0;width:711px;height:157px;display:flex;padding:18px 22px}
.intro h1{font-family:"Montserrat",sans-serif;font-weight:600;font-size:20px;line-height:1.2;color:var(--blue);width:270px}
.intro-copy{margin-left:auto;width:340px}
.intro-copy h2{font-family:"Montserrat",sans-serif;font-weight:700;font-size:9px;color:var(--navy);text-align:right;margin-bottom:6px;line-height:1.3}
.intro-copy p{font-size:6.5px;line-height:1.55;color:var(--muted);text-align:justify}
.why{position:absolute;top:503px;left:0;width:711px;height:697px;background:var(--blue);color:var(--white);text-align:center;padding:30px 56px;display:flex;flex-direction:column;justify-content:space-evenly}
.why-item h3{font-family:"Montserrat",sans-serif;font-weight:700;font-size:11px;margin-bottom:5px}
.why-item p{font-size:9px;line-height:1.6}
</style>
</head>
<body>
<header class="site-header">
  <div class="brand"><span class="brand-mark"></span>Corwist Lane Injury Lawyers</div>
  <nav class="main-nav"><span>About Us</span><span>Cases We Handle</span><span>Locations</span><span>Resources</span><span>Contact</span></nav>
  <div class="header-cta">602-555-0148</div>
</header>

<section class="hero">
  <div class="hero-photo" role="img" aria-label="Portrait of a smiling attorney in a suit"></div>
  <ul class="hero-checks">
    <li><span class="tick"><svg width="7" height="7" viewBox="0 0 10 10"><path d="M1.5 5.2l2.3 2.3L8.5 2.5" fill="none" stroke="#fff" stroke-width="1.8"/></svg></span>Phoenix Personal Injury Lawyers</li>
    <li><span class="tick"><svg width="7" height="7" viewBox="0 0 10 10"><path d="M1.5 5.2l2.3 2.3L8.5 2.5" fill="none" stroke="#fff" stroke-width="1.8"/></svg></span>99% Success Rate</li>
    <li><span class="tick"><svg width="7" height="7" viewBox="0 0 10 10"><path d="M1.5 5.2l2.3 2.3L8.5 2.5" fill="none" stroke="#fff" stroke-width="1.8"/></svg></span>550+ 5-Star Reviews</li>
    <li><span class="tick"><svg width="7" height="7" viewBox="0 0 10 10"><path d="M1.5 5.2l2.3 2.3L8.5 2.5" fill="none" stroke="#fff" stroke-width="1.8"/></svg></span>$0 Fee Unless We Win</li>
  </ul>
  <div class="hero-btn">GET YOUR FREE CONSULTATION</div>
</section>

<section class="media">
  <p class="media-label">We are the legal experts the media calls</p>
  <div class="media-logos">
    <span style="width:16px"></span><span style="width:16px"></span><span style="width:22px"></span><span style="width:18px"></span><span style="width:18px"></span><span style="width:16px"></span><span style="width:16px"></span><span style="width:62px"></span>
  </div>
  <div class="trust">
    <div class="trust-badge"><i></i><b></b></div>
    <div class="trust-badge"><i></i><b></b></div>
    <div class="trust-badge"><i></i><b></b></div>
  </div>
</section>

<div class="scene" role="img" aria-label="Aftermath of a car accident on a city street"></div>

<nav class="practice-bar">
  <a>Car Accident Lawyer in Phoenix</a>
  <a>Truck Accident Lawyer in Phoenix</a>
  <a>Motorcycle Accident Lawyer in Phoenix</a>
  <a>Motorcycle Accident Lawyer in Phoenix</a>
  <a>Pedestrian Accident Lawyer in Phoenix</a>
  <a>Wrongful Death Lawyer in Phoenix</a>
</nav>

<section class="intro">
  <h1>Top-Rated Phoenix Personal Injury Attorneys With A 99% Success Rate</h1>
  <div class="intro-copy">
    <h2>Helping Injury Victims Across Phoenix and the Valley<br>Recover and Rebuild</h2>
    <p>Every year, thousands of people in Phoenix and across the Valley suffer serious injuries due to preventable accidents — from unsafe property conditions and workplace incidents to defective products, medical malpractice, and dog bites. Many victims never pursue the compensation they're entitled to. At Corwist Lane Injury Lawyers, our personal injury attorneys help clients throughout Phoenix, Scottsdale, Mesa, and beyond take the first step toward justice and recovery... »</p>
  </div>
</section>

<section class="why">
  <div class="why-item">
    <h3>Why We're Phoenix's Top-Rated Personal Injury Law Firm</h3>
    <p>As a distinguished division of Harwell Stone, P.C.—Arizona's oldest law firm, established in 1885—our Phoenix legal team carries a level of institutional credibility that few others can match. Over generations, Harwell Stone has built trusted relationships with judges, juries, and legal professionals across Maricopa County, earning a reputation for integrity, excellence, and results. When you work with Corwist Lane Injury Lawyers, you benefit not just from aggressive representation, but from the unmatched legal reputation of a firm deeply woven into Arizona's legal fabric. Our legal team is trusted by clients across Phoenix, Scottsdale, Mesa, Glendale, and Chandler — and known for securing exceptional results in high-stakes injury cases.</p>
  </div>
  <div class="why-item">
    <h3>Millions Recovered</h3>
    <p>Our Phoenix personal injury lawyers have secured substantial verdicts and settlements across Arizona in complex injury claims — from serious falls to catastrophic injuries.</p>
  </div>
  <div class="why-item">
    <h3>99% Success Rate</h3>
    <p>Our track record speaks volumes. From the settlement table to courtroom, we deliver results.</p>
  </div>
  <div class="why-item">
    <h3>Client-Focused Approach</h3>
    <p>Our injury attorneys serve Phoenix and the surrounding areas with compassion, communication, and transparency at every step.</p>
  </div>
  <div class="why-item">
    <h3>No-Fee Promise</h3>
    <p>You never pay unless we win — our no-fee promise applies to all personal injury cases across Phoenix, Scottsdale, Mesa, and beyond.</p>
  </div>
</section>
</body>
</html>
```